Custom Truck shop New Business Card design

double sided business card including my new logo, brand colors and picking a font I attached, clean and modern look. I attached the old card for some reference. and would like to include the picture of the white truck attached. I would also like to have it with one of my employees info as well. (same info except name and title Brin Tolvay Service Writer)

Dale Porvick
Owner

address
48310 E Calloway Ridge Rd S
STE 217
Marsh Hollow, CO 80219

phone 720-555-0184

email dale@brokenspurrigs.example

website brokenspurrgis.example

social @brokenspurrigs

Target Market(s)

men 18-60

Industry/Entity Type

Automotive

Contact Information for Business Card

Dale Porvick Owner address 48310 E Calloway Ridge Rd S STE 217 Marsh Hollow, CO 80219 phone 720-555-0184 email dale@brokenspurrigs.example website brokenspurrgis.example social @brokenspurrigs

Font styles to use
Other font styles liked:
• fonts attached

Requirements
Must have
• new logo, orange #FC68D, Charcoal #333333
Nice to have
• the white truck

```html
<!DOCTYPE html>
<html lang="en">
<head>
<meta charset="utf-8">
<title>Broken Spur Rigs – Business Card</title>
<link rel="stylesheet" href="https://fonts.googleapis.com/css2?family=Jost:wght@500;700&family=Kanit:ital,wght@1,600;1,800&display=swap">
<style>
  :root {
    --orange: #fc6a2e;
    --charcoal: #333333;
    --paper: #ffffff;
    --backdrop: #ededed;
    --photo-light: #d9dbde;
    --photo-dark: #3a3b3f;
  }
  html, body {
    margin: 0;
    width: 1200px;
    height: 1200px;
    overflow: hidden;
    background: var(--backdrop);
  }
  .stage {
    position: relative;
    width: 1200px;
    height: 1200px;
  }
  .card {
    position: absolute;
    left: 181px;
    width: 838px;
    height: 478px;
    display: block;
  }
  .card--front { top: 110px; }
  .card--back { top: 611px; }
  .brand-name {
    font-family: "Jost", sans-serif;
    font-weight: 500;
    fill: var(--orange);
    letter-spacing: 4px;
  }
  .brand-name--small {
    fill: var(--charcoal);
    letter-spacing: 1px;
  }
  .person-name {
    font-family: "Kanit", sans-serif;
    font-style: italic;
    font-weight: 800;
    fill: var(--charcoal);
  }
  .person-title {
    font-family: "Jost", sans-serif;
    font-weight: 700;
    fill: var(--orange);
  }
  .contact-line {
    font-family: "Kanit", sans-serif;
    font-style: italic;
    font-weight: 600;
    fill: #111111;
    font-size: 27px;
  }
  .rule { stroke: var(--orange); stroke-width: 3; }
  .icon { fill: none; stroke: var(--paper); stroke-width: 3.5; stroke-linecap: round; stroke-linejoin: round; }
  .icon-solid { fill: var(--paper); }
</style>
</head>
<body>
<main class="stage">

  <!-- Front side -->
  <svg class="card card--front" viewBox="0 0 1348 770" xmlns="http://www.w3.org/2000/svg">
    <rect width="1348" height="770" fill="var(--charcoal)"/>
    <polygon class="band band--top" points="291,0 1056,0 1008,50 340,50" fill="var(--orange)"/>
    <polygon class="band band--bottom" points="340,720 1008,720 1056,770 291,770" fill="var(--orange)"/>
    <text class="brand-name" x="674" y="412" font-size="84" text-anchor="middle">BROKEN SPUR RIGS</text>
  </svg>

  <!-- Back side -->
  <svg class="card card--back" viewBox="0 0 1348 770" xmlns="http://www.w3.org/2000/svg">
    <rect width="1348" height="770" fill="var(--paper)"/>

    <!-- name block -->
    <rect class="accent-bar" x="0" y="0" width="51" height="170" fill="var(--orange)"/>
    <path class="name-tab" d="M0 158 H120 a10 10 0 0 1 10 10 V261 a10 10 0 0 1 -10 10 H0 Z" fill="var(--orange)"/>
    <circle class="icon-solid" cx="73" cy="200" r="13"/>
    <path class="icon-solid" d="M52 241 a21 21 0 0 1 42 0 V242 H52 Z"/>
    <text class="person-name" x="155" y="220" font-size="64">Dale Porvick</text>
    <text class="person-title" x="155" y="264" font-size="36">Owner</text>

    <!-- brand mark -->
    <circle cx="1139" cy="160" r="86" fill="var(--charcoal)"/>
    <text class="brand-name brand-name--small" x="1139" y="282" font-size="26" text-anchor="middle">BROKEN SPUR RIGS</text>

    <!-- contact sidebar -->
    <path class="contact-rail" d="M0 345 H110 a10 10 0 0 1 10 10 V770 H0 Z" fill="var(--charcoal)"/>

    <!-- mail -->
    <rect class="icon" x="56" y="375" width="38" height="26" rx="3"/>
    <path class="icon" d="M56 378 L75 392 L94 378"/>
    <!-- globe -->
    <circle class="icon" cx="75" cy="456" r="17"/>
    <ellipse class="icon" cx="75" cy="456" rx="7" ry="17"/>
    <path class="icon" d="M58 456 H92 M61 447 H89 M61 465 H89"/>
    <!-- phone -->
    <path class="icon" d="M64 508 l7 -2 l5 10 l-5 4 q4 8 11 12 l4 -5 l10 5 l-2 7 q-16 2 -27 -10 q-8 -10 -3 -21 Z"/>
    <!-- social -->
    <rect class="icon" x="58" y="572" width="34" height="34" rx="9"/>
    <circle class="icon" cx="75" cy="589" r="8"/>
    <!-- pin -->
    <path class="icon-solid" d="M75 637 a16 16 0 0 1 16 16 c0 12 -16 28 -16 28 c0 0 -16 -16 -16 -28 a16 16 0 0 1 16 -16 Z"/>
    <circle cx="75" cy="652" r="6" fill="var(--charcoal)"/>

    <text class="contact-line" x="145" y="393">dale@brokenspurrigs.example</text>
    <line class="rule" x1="145" y1="407" x2="594" y2="407"/>
    <text class="contact-line" x="145" y="460">www.brokenspurrgis.example</text>
    <line class="rule" x1="145" y1="475" x2="570" y2="475"/>
    <text class="contact-line" x="145" y="530">720-555-0184</text>
    <line class="rule" x1="145" y1="543" x2="366" y2="543"/>
    <text class="contact-line" x="145" y="596">www.brokenspurrgis.example</text>
    <line class="rule" x1="145" y1="609" x2="570" y2="609"/>
    <text class="contact-line" x="145" y="660">48310 E Calloway Ridge Rd S</text>
    <text class="contact-line" x="145" y="691">STE 217</text>
    <text class="contact-line" x="145" y="722">Marsh Hollow, CO 80219</text>
    <line class="rule" x1="145" y1="737" x2="586" y2="737"/>

    <!-- truck photo area -->
    <defs>
      <linearGradient id="truckPhotoTone" x1="0" y1="0" x2="0" y2="1">
        <stop offset="0" stop-color="var(--photo-light)"/>
        <stop offset="0.55" stop-color="#a9abb0"/>
        <stop offset="1" stop-color="var(--photo-dark)"/>
      </linearGradient>
    </defs>
    <polygon role="img" aria-label="Photo of a lifted white pickup truck with chrome wheels parked in a lot"
             points="700,345 1348,345 1348,770 652,770" fill="url(#truckPhotoTone)"/>
  </svg>

</main>
</body>
</html>
```